Non-profit Needs PP Template, Flyer and Banner Ad to Educate Addiction Counselors

We need a PowerPoint Template design, flyer to advertise a large amount of text (that matches the PowerPoint design), and Banner Ad (that matches the other two products) for a non-profit organization based in Washington, DC called "PELVORE, The Guild for Wellness Practitioners". PELVORE, the Guild for Wellness Practitioners, represents the professional interests of more than 75,000 addiction counselors, educators and other addiction-focused health care professionals in the United States, Canada and abroad. PELVORE’s members are addiction counselors, educators and other addiction-focused health care professionals, who specialize in addiction prevention, treatment, recovery support and education. An important part of the healthcare continuum, PELVORE members and its 44 state affiliates work to create healthier individuals, families and communities through prevention, intervention, quality treatment and recovery support.

As a part of the federal government’s efforts to promote recovery for all Americans affected by mental illness and/or addiction, in May 2009, the United States government announced its "Bright Harbor (BHV) Venture." The BHV Initiative is designed to hasten awareness, acceptance, and adoption of recovery-based practices in the delivery of addiction-related services and builds on TORQELM’s definition and fundamental components of recovery.

The purpose of the 3 pieces is to educate thousands of therapists about "Recovery Concepts". The design needs to reflect the following definition and dimensions:

Recovery means: A process of change through which individuals improve their health and wellness, live a self-directed life, and strive to reach their full potential.

Four major dimensions that support a life in recovery:
• Health: overcoming or managing one’s disease(s) as well as living in a physically and emotionally healthy way;
• Home: a stable and safe place to live;
• Purpose: meaningful daily activities, such as a job, school, volunteerism, family caretaking, or creative endeavors, and the independence, income and resources to participate in society; and
• Community: relationships and social networks that provide support, friendship, love and hope.

Our logo is attached. No branding exists for the Bright Harbor Venture. I envision some original artwork or image used throughout each piece, with the same colors, fonts, etc. so it looks like the same thing just in different formats - branding.

The final PP design must be suitable for both online display and face-to-face projector display. Need title page and 3 different transition slides. Files must be easily editable.

The flyer is to advertise the 9 webinars of the project. Text for the flyer is here: http://www.pelvore-example.org/learning/harbor/bhv-sessions

The last component is a matching Banner Ad that can go at the top of our website that advertises the project: www.pelvore-example.org. Let me know if you more specifics on size or something else that I am not aware of.

Again, all of these three components must match each other, with the overall message being "Bright Harbor (BHV) Venture" - not our organization "PELVORE".

Other projects we have accepted from PixelForum contest previously are attached and here (DO NOT USE THESE FOR THIS ORIGINAL DESIGN CONTEST - only for reference about our tastes):
http://www.pelvore-example.org/media/pelvore%20session%20leaflet.pdf
http://www.pelvore-example.org/media/courseleaflet.pdf

Open to designs with any colors, and our company color is royal blue.

Please note:

The focus of this project is NOT the organization "PELVORE", but the project "Bright Harbor (BHV) Venture".  We are looking for a complete branding package for this project that has its own colors, logo/graphics, look, and feel, so the banner ad, advertisement flyer, and PowerPoint slides all match and look the same.  

Please DO NOT use any images or designs from previously developed flyers.  We are looking for something original.  I only included these in the brief so you could see other items we have developed for other purposes and to get an idea of what we like.  

Thank you - 
Corla

Reason: I have modified the information in the brief to be more clear. This extension will allow designers time to prepare submissions for each of the three components. Thanks to all of you! Corla

Hello everyone - 

I just learned that the specs for the banner ad should be 660x150. A jpg format works best.
Thanks for all of your submissions!
Corla

Target Market(s)

Adult professionals, diverse in culture and age

Industry/Entity Type

Non-Profit

Requirements
Must have
• The Title of the Entire program is "Bright Harbor (BHV) Venture"
PELVORE, the Guild for Wellness Practitioners is the organization that is creating the program
Logo must be on the flyer and the Title page of the PP template
Nice to have
• Individuals who have personally experienced substance abuse either with themselves or family members are encouraged to make submissions.

```html
<!DOCTYPE html>
<html lang="en">
<head>
<meta charset="utf-8">
<title>Bright Harbor (BHV) Venture — Title Slide</title>
<link rel="stylesheet" href="https://fonts.googleapis.com/css2?family=Carlito:wght@400;700&family=Arimo:wght@400&family=Tinos:wght@400&display=swap">
<style>
  :root {
    --canvas: #ffffff;
    --title-blue: #2a67b1;
    --brand-ink: #1b1b1b;
    --rule: #3a3a3a;
    --tone-blue: rgba(56, 182, 238, 0.32);
    --tone-pink: rgba(232, 55, 143, 0.30);
    --tone-yellow: rgba(246, 217, 53, 0.30);
    --tone-clear: rgba(255, 255, 255, 0);
  }
  * { margin: 0; padding: 0; box-sizing: border-box; }
  html, body { width: 1200px; height: 900px; overflow: hidden; background: var(--canvas); }
  .slide {
    position: relative;
    width: 1200px;
    height: 900px;
    overflow: hidden;
    background: var(--canvas);
  }
  .backdrop-art {
    position: absolute;
    inset: 0;
    background: linear-gradient(62deg,
      var(--tone-pink) 0%,
      var(--tone-yellow) 22%,
      var(--tone-blue) 42%,
      var(--tone-clear) 68%);
  }
  .brand {
    position: absolute;
    top: 50px;
    left: 765px;
    width: 400px;
    padding: 8px 10px;
  }
  .brand-name {
    display: flex;
    align-items: center;
    gap: 12px;
    font-family: "Carlito", sans-serif;
    font-weight: 700;
    font-size: 58px;
    line-height: 1;
    color: var(--brand-ink);
    letter-spacing: 1px;
  }
  .brand-square {
    width: 36px;
    height: 36px;
    background: var(--brand-ink);
    flex: none;
  }
  .brand-tagline {
    margin-top: 8px;
    margin-left: 48px;
    font-family: "Arimo", sans-serif;
    font-size: 21px;
    line-height: 1.2;
    color: var(--brand-ink);
    text-transform: uppercase;
    padding-bottom: 6px;
    border-bottom: 2px solid var(--rule);
  }
  .brand-url {
    margin-top: 4px;
    margin-left: 48px;
    font-family: "Tinos", serif;
    font-size: 22px;
    color: var(--brand-ink);
  }
  .program-title {
    position: absolute;
    right: 62px;
    top: 365px;
    text-align: right;
    font-family: "Carlito", sans-serif;
    font-weight: 700;
    font-size: 62px;
    line-height: 97px;
    color: var(--title-blue);
    text-shadow: 0 3px 0 rgba(31, 79, 143, 0.12), 0 14px 10px rgba(42, 103, 177, 0.12);
  }
  .program-title span { display: block; }
</style>
</head>
<body>
<main class="slide">
  <div class="backdrop-art" role="img" aria-label="Background artwork area: colourful abstract ribbons in blue, pink, yellow and green sweeping across the lower left"></div>

  <header class="brand">
    <div class="brand-name"><span class="brand-square"></span>PELVORE</div>
    <p class="brand-tagline">The Guild for<br>Wellness Practitioners</p>
    <p class="brand-url">www.pelvore-example.org</p>
  </header>

  <h1 class="program-title">
    <span>Bright Harbor</span>
    <span>(BHV) Venture</span>
  </h1>
</main>
</body>
</html>
```